Halvorsen Basin Holdings, LP Letter Head

We need an official company letter head design that is clean and mimics our company logo style. It will include our logo, address, phone, and website. We are an OIl and Gas mineral purchasing company, so hints of oil rigs or related design would be desirable.

Industry/Entity Type

Oil And Gas

Colors
ec1f27
f04a50
f59195
fbd4d5

Requirements
Must have
• Logo
• 7316 Marwick T. Ellsbury Parkway, Suite 418
• Dallas TX, 75391
• 214-763-1957
• www.halvorsenbasin.com
Nice to have
• Oil Rigs or OIl and gas related design

```html
<!DOCTYPE html>
<html lang="en">
<head>
<meta charset="utf-8">
<title>Halvorsen Basin Holdings, LP Letterhead</title>
<link rel="stylesheet" href="https://fonts.googleapis.com/css2?family=Cinzel:wght@400;600&display=swap">
<style>
  :root {
    --red: #ec1f27;
    --red-mid: #f04a50;
    --red-soft: #f59195;
    --red-pale: #fbd4d5;
    --paper: #ececec;
    --desk: #c8c9cb;
    --rig-tone: #dedede;
    --white: #ffffff;
  }
  * { margin: 0; padding: 0; box-sizing: border-box; }
  html, body {
    width: 1200px;
    height: 800px;
    overflow: hidden;
    background: var(--desk);
  }
  .letterhead {
    position: absolute;
    left: 338px;
    top: 30px;
    width: 524px;
    height: 740px;
    background: var(--paper);
    overflow: hidden;
    box-shadow: 0 2px 10px rgba(0,0,0,0.12);
    font-family: "Cinzel", serif;
  }
  .header-swoosh {
    position: absolute;
    top: 0;
    left: 0;
    width: 524px;
    height: 250px;
  }
  .brand {
    position: absolute;
    left: 40px;
    top: 20px;
    width: 190px;
    display: flex;
    flex-direction: column;
    align-items: center;
    gap: 6px;
  }
  .brand-square {
    width: 34px;
    height: 34px;
    background: var(--red);
  }
  .brand-name {
    color: var(--red);
    font-weight: 600;
    font-size: 13px;
    letter-spacing: 0.04em;
    white-space: nowrap;
  }
  .contact {
    position: absolute;
    right: 14px;
    top: 108px;
    display: flex;
    flex-direction: column;
    gap: 5px;
    color: var(--white);
    font-size: 9px;
    letter-spacing: 0.03em;
    text-align: right;
  }
  .contact-row {
    display: flex;
    align-items: center;
    justify-content: flex-end;
    gap: 8px;
  }
  .contact-icon {
    width: 15px;
    height: 15px;
    flex: none;
  }
  .rig-scene {
    position: absolute;
    left: 40px;
    top: 360px;
    width: 260px;
    height: 318px;
    background: linear-gradient(180deg, rgba(222,222,222,0) 0%, var(--rig-tone) 45%, var(--rig-tone) 100%);
  }
  .footer-band {
    position: absolute;
    left: 0;
    bottom: 0;
    width: 100%;
    height: 62px;
    background: var(--red);
  }
</style>
</head>
<body>
  <main class="letterhead">
    <svg class="header-swoosh" viewBox="0 0 524 250" aria-hidden="true">
      <path d="M250,0 H524 V246 H430 C320,226 250,140 250,0 Z" fill="var(--red-pale)"/>
      <path d="M282,0 H524 V240 H450 C345,222 282,140 282,0 Z" fill="var(--red-soft)"/>
      <path d="M316,0 H524 V234 H470 C370,218 316,140 316,0 Z" fill="var(--red)"/>
    </svg>

    <div class="brand">
      <div class="brand-square"></div>
      <div class="brand-name">Halvorsen Basin Holdings</div>
    </div>

    <div class="contact">
      <div class="contact-row">
        <span>214-763-1957</span>
        <svg class="contact-icon" viewBox="0 0 16 16" aria-hidden="true">
          <circle cx="8" cy="8" r="7.5" fill="var(--white)"/>
          <path d="M5.3,4 L6.8,4 L7.3,6.2 L6.4,6.9 C6.9,8 7.9,9 9,9.5 L9.7,8.6 L11.9,9.1 L11.9,10.6 C11.9,11.2 11.4,11.6 10.8,11.5 C7.6,11.1 4.8,8.3 4.4,5.1 C4.3,4.5 4.7,4 5.3,4 Z" fill="var(--red)"/>
        </svg>
      </div>
      <div class="contact-row">
        <span>www.halvorsenbasin.com</span>
        <svg class="contact-icon" viewBox="0 0 16 16" aria-hidden="true">
          <circle cx="8" cy="8" r="7.5" fill="var(--white)"/>
          <g fill="none" stroke="var(--red)" stroke-width="1">
            <circle cx="8" cy="8" r="4"/>
            <ellipse cx="8" cy="8" rx="1.8" ry="4"/>
            <line x1="4" y1="8" x2="12" y2="8"/>
          </g>
        </svg>
      </div>
      <div class="contact-row">
        <span>7316 Marwick T. Ellsbury Parkway, Suite 418<br>Dallas TX, 75391</span>
        <svg class="contact-icon" viewBox="0 0 16 16" aria-hidden="true">
          <circle cx="8" cy="8" r="7.5" fill="var(--white)"/>
          <path d="M8,3.8 L12.2,7.6 L11,7.6 L11,11.6 L9,11.6 L9,9.2 L7,9.2 L7,11.6 L5,11.6 L5,7.6 L3.8,7.6 Z" fill="var(--red)"/>
        </svg>
      </div>
    </div>

    <div class="rig-scene" role="img" aria-label="Faint silhouette of an offshore oil rig and pumpjacks"></div>

    <div class="footer-band"></div>
  </main>
</body>
</html>
```